Car wash line needed for the pylon inscription

We need a design template / print template for our advertising pylon so that the Plavex plates can be printed. The area to be printed is approx. 1.5m wide and approx. 2.70m high. We operate a car wash about 30m long. The washing rollers are equipped with scratch-free Silkren Tuft foam material. Before the vehicle is put into the car wash it gets a manual high pressure pre-wash. There are four different washing programs: basic laundry € 7.50 (wheel cleaning, intensive washing, gloss drying comfort care € 10.50 (like base + active foam) special care € 13.00 (like comfort + glossy sealing with lotus wax) premium care € 15.50 (like special care + Underbody wash) The pylon is right on the driveway on a busy road, we want to achieve maximum attention with the pylons. It should not be too much content because the vehicles drive past it, due to an immediate gyro, the speed is however at about 40Km / h. Opening hours Mon-Fri. 08: 00-19: 00 Sat 07: 00-19: 00 The Plavex plates are red. The enclosed files show our pylon with a little appealing design proposal our advertising agency and the real local places. For the opinion you can see on the following link a youtube video with a comparable car wash like ours, the washing process is well illustrated there. https://www.clipvaro.net/view?v=Qk7rTm2LpZa Furthermore, we have a bonus card system who has washed our car 10 times gets the 11 laundry for free. From foam additives we use active foam from the comfort care and from the special care gets the vehicle lotus wax, which has the effect that the paint is sealed and keeps the shine longer. We need a design template / print template for our advertising pylon so that the Plavex plates can be printed. The area to be printed is approx. 1.5m wide and approx. 2.70m high. We operate a car wash about 30m long. The washing rollers are equipped with scratch-free Silkren Tuft foam material. Before the vehicle is put into the car wash it gets a manual high pressure pre-wash. There are four different washing programs: basic laundry € 7.50 (wheel cleaning, intensive washing, gloss drying comfort care € 10.50 (like base + active foam) special care € 13.00 (like comfort + glossy sealing with lotus wax) premium care € 15.50 (like special care + Underbody wash) The pylon is right on the driveway on a busy road, we want to achieve maximum attention with the pylons. It should not be too much content because the vehicles drive past it, due to an immediate gyro, the speed is however at about 40Km / h. Opening hours Mon-Fri. 08: 00-19: 00 Sat 07: 00-19: 00 The Plavex plates are red. The enclosed files show our pylon with a little appealing design proposal our advertising agency and the real local places. For the opinion you can see on the following link a youtube video with a comparable car wash like ours, the washing process is well illustrated there. https://www.clipvaro.net/view?v=Qk7rTm2LpZa Furthermore, we have a bonus card system who has washed our car 10 times gets the 11 laundry for free. From foam additives we use active foam from the comfort care and from the special care gets the vehicle lotus wax, which has the effect that the paint is sealed and keeps the shine longer. We need a design template / print template for our advertising pylon so that the Plavex plates can be printed. The area to be printed is approx. 1.5m wide and approx. 2.70m high. We operate a car wash about 30m long. The washing rollers are equipped with scratch-free Silkren Tuft foam material. Before the vehicle is put into the car wash it gets a manual high pressure pre-wash. There are four different washing programs: basic laundry € 7.50 (wheel cleaning, intensive washing, gloss drying comfort care € 10.50 (like base + active foam) special care € 13.00 (like comfort + glossy sealing with lotus wax) premium care € 15.50 (like special care + Underbody wash) The pylon is right on the driveway on a busy road, we want to achieve maximum attention with the pylons. It should not be too much content because the vehicles drive past it, due to an immediate gyro, the speed is however at about 40Km / h. Opening hours Mon-Fri. 08: 00-19: 00 Sat 07: 00-19: 00 The Plavex plates are red. The enclosed files show our pylon with a little appealing design proposal our advertising agency and the real local places. For the opinion you can see on the following link a youtube video with a comparable car wash like ours, the washing process is well illustrated there. https://www.clipvaro.net/view?v=Qk7rTm2LpZa Furthermore, we have a bonus card system who has washed our car 10 times gets the 11 laundry for free. From foam additives we use active foam from the comfort care and from the special care gets the vehicle lotus wax, which has the effect that the paint is sealed and keeps the shine longer. We need a design template / print template for our advertising pylon so that the Plavex plates can be printed. The area to be printed is approx. 1.5m wide and approx. 2.70m high. We operate a car wash about 30m long. The washing rollers are equipped with scratch-free Silkren Tuft foam material. Before the vehicle is put into the car wash it gets a manual high pressure pre-wash. There are four different washing programs: basic laundry € 7.50 (wheel cleaning, intensive washing, gloss drying comfort care € 10.50 (like base + active foam) special care € 13.00 (like comfort + glossy sealing with lotus wax) premium care € 15.50 (like special care + Underbody wash) The pylon is right on the driveway on a busy road, we want to achieve maximum attention with the pylons. It should not be too much content because the vehicles drive past it, due to an immediate gyro, the speed is however at about 40Km / h. Opening hours Mon-Fri. 08: 00-19: 00 Sat 07: 00-19: 00 The Plavex plates are red. The enclosed files show our pylon with a little appealing design proposal our advertising agency and the real local places. For the opinion you can see on the following link a youtube video with a comparable car wash like ours, the washing process is well illustrated there. https://www.clipvaro.net/view?v=Qk7rTm2LpZa Furthermore, we have a bonus card system who has washed our car 10 times gets the 11 laundry for free. From foam additives we use active foam from the comfort care and from the special care gets the vehicle lotus wax, which has the effect that the paint is sealed and keeps the shine longer. We need a design template / print template for our advertising pylon so that the Plavex plates can be printed. The area to be printed is approx. 1.5m wide and approx. 2.70m high. We operate a car wash about 30m long. The washing rollers are equipped with scratch-free Silkren Tuft foam material. Before the vehicle is put into the car wash it gets a manual high pressure pre-wash. There are four different washing programs: basic laundry € 7.50 (wheel cleaning, intensive washing, gloss drying comfort care € 10.50 (like base + active foam) special care € 13.00 (like comfort + glossy sealing with lotus wax) premium care € 15.50 (like special care + Underbody wash) The pylon is right on the driveway on a busy road, we want to achieve maximum attention with the pylons. It should not be too much content because the vehicles drive past it, due to an immediate gyro, the speed is however at about 40Km / h. Opening hours Mon-Fri. 08: 00-19: 00 Sat 07: 00-19: 00 The Plavex plates are red. The enclosed files show our pylon with a little appealing design proposal our advertising agency and the real local places. For the opinion you can see on the following link a youtube video with a comparable car wash like ours, the washing process is well illustrated there. https://www.clipvaro.net/view?v=Qk7rTm2LpZa Furthermore, we have a bonus card system who has washed our car 10 times gets the 11 laundry for free. From foam additives we use active foam from the comfort care and from the special care gets the vehicle lotus wax, which has the effect that the paint is sealed and keeps the shine longer. We need a design template / print template for our advertising pylon so that the Plavex plates can be printed. The area to be printed is approx. 1.5m wide and approx. 2.70m high. We operate a car wash about 30m long. The washing rollers are equipped with scratch-free Silkren Tuft foam material. Before the vehicle is put into the car wash it gets a manual high pressure pre-wash. There are four different washing programs: basic laundry € 7.50 (wheel cleaning, intensive washing, gloss drying comfort care € 10.50 (like base + active foam) special care € 13.00 (like comfort + glossy sealing with lotus wax) premium care € 15.50 (like special care + Underbody wash) The pylon is right on the driveway on a busy road, we want to achieve maximum attention with the pylons. It should not be too much content because the vehicles drive past it, due to an immediate gyro, the speed is however at about 40Km / h. Opening hours Mon-Fri. 08: 00-19: 00 Sat 07: 00-19: 00 The Plavex plates are red. The enclosed files show our pylon with a little appealing design proposal our advertising agency and the real local places. For the opinion you can see on the following link a youtube video with a comparable car wash like ours, the washing process is well illustrated there. https://www.clipvaro.net/view?v=Qk7rTm2LpZa Furthermore, we have a bonus card system who has washed our car 10 times gets the 11 laundry for free. From foam additives we use active foam from the comfort care and from the special care gets the vehicle lotus wax, which has the effect that the paint is sealed and keeps the shine longer. We need a design template / print template for our advertising pylon so that the Plavex plates can be printed. The area to be printed is approx. 1.5m wide and approx. 2.70m high. We operate a car wash about 30m long. The washing rollers are equipped with scratch-free Silkren Tuft foam material. Before the vehicle is put into the car wash it gets a manual high pressure pre-wash. There are four different washing programs: basic laundry € 7.50 (wheel cleaning, intensive washing, gloss drying comfort care € 10.50 (like base + active foam) special care € 13.00 (like comfort + glossy sealing with lotus wax) premium care € 15.50 (like special care + Underbody wash) The pylon is right on the driveway on a busy road, we want to achieve maximum attention with the pylons. It should not be too much content because the vehicles drive past it, due to an immediate gyro, the speed is however at about 40Km / h. Opening hours Mon-Fri. 08: 00-19: 00 Sat 07: 00-19: 00 The Plavex plates are red. The enclosed files show our pylon with a little appealing design proposal our advertising agency and the real local places. For the opinion you can see on the following link a youtube video with a comparable car wash like ours, the washing process is well illustrated there. https://www.clipvaro.net/view?v=Qk7rTm2LpZa Furthermore, we have a bonus card system who has washed our car 10 times gets the 11 laundry for free. From foam additives we use active foam from the comfort care and from the special care gets the vehicle lotus wax, which has the effect that the paint is sealed and keeps the shine longer. We need a design template / print template for our advertising pylon so that the Plavex plates can be printed. The area to be printed is approx. 1.5m wide and approx. 2.70m high. We operate a car wash about 30m long. The washing rollers are equipped with scratch-free Silkren Tuft foam material. Before the vehicle is put into the car wash it gets a manual high pressure pre-wash. There are four different washing programs: basic laundry € 7.50 (wheel cleaning, intensive washing, gloss drying comfort care € 10.50 (like base + active foam) special care € 13.00 (like comfort + glossy sealing with lotus wax) premium care € 15.50 (like special care + Underbody wash) The pylon is right on the driveway on a busy road, we want to achieve maximum attention with the pylons. It should not be too much content because the vehicles drive past it, due to an immediate gyro, the speed is however at about 40Km / h. Opening hours Mon-Fri. 08: 00-19: 00 Sat 07: 00-19: 00 The Plavex plates are red. The enclosed files show our pylon with a little appealing design proposal our advertising agency and the real local places. For the opinion you can see on the following link a youtube video with a comparable car wash like ours, the washing process is well illustrated there. https://www.clipvaro.net/view?v=Qk7rTm2LpZa Furthermore, we have a bonus card system who has washed our car 10 times gets the 11 laundry for free. From foam additives we use active foam from the comfort care and from the special care gets the vehicle lotus wax, which has the effect that the paint is sealed and keeps the shine longer. We need a design template / print template for our advertising pylon so that the Plavex plates can be printed. The area to be printed is approx. 1.5m wide and approx. 2.70m high. We operate a car wash about 30m long. The washing rollers are equipped with scratch-free Silkren Tuft foam material. Before the vehicle is put into the car wash it gets a manual high pressure pre-wash. There are four different washing programs: basic laundry € 7.50 (wheel cleaning, intensive washing, gloss drying comfort care € 10.50 (like base + active foam) special care € 13.00 (like comfort + glossy sealing with lotus wax) premium care € 15.50 (like special care + Underbody wash) The pylon is right on the driveway on a busy road, we want to achieve maximum attention with the pylons. It should not be too much content because the vehicles drive past it, due to an immediate gyro, the speed is however at about 40Km / h. Opening hours Mon-Fri. 08: 00-19: 00 Sat 07: 00-19: 00 The Plavex plates are red. The enclosed files show our pylon with a little appealing design proposal our advertising agency and the real local places. For the opinion you can see on the following link a youtube video with a comparable car wash like ours, the washing process is well illustrated there. https://www.clipvaro.net/view?v=Qk7rTm2LpZa Furthermore, we have a bonus card system who has washed our car 10 times gets the 11 laundry for free. From foam additives we use active foam from the comfort care and from the special care gets the vehicle lotus wax, which has the effect that the paint is sealed and keeps the shine longer.
Updates

Target Market(s)

germany

Colors

Designer to choose colors to be used in the design.

Requirements
Must have
• Print template for the print job in the accepted formats. Of course, the design must be in German
Nice to have
• Colors that attract attention, but are still serious. The content must be perceived when passing by and the customers must be aware of the car wash.
Should not have
• Kitschiges Design Too much content which takes longer to be read.

```html
<!DOCTYPE html>
<html lang="de">
<head>
<meta charset="utf-8">
<title>Glanzstraße am Lindenhof – Pylon</title>
<link rel="stylesheet" href="https://fonts.googleapis.com/css2?family=Anton&family=Roboto+Condensed:wght@800;900&display=swap">
<style>
  :root{
    --sign-red:#c22d32;
    --sign-grey:#6f7074;
    --sign-edge:#e4e4e6;
    --frame:#30333b;
    --navy:#0f2f80;
    --navy-deep:#0a2470;
    --foam:#ffffff;
    --sun:#f3d41a;
    --hours-red:#e02020;
    --bg:#ffffff;
  }
  html,body{margin:0;padding:0;overflow:hidden;background:var(--bg);}
  .canvas{width:780px;height:1200px;position:relative;}
  .canvas svg{display:block;}
  .brand-name{font-family:"Anton",sans-serif;fill:var(--foam);}
  .brand-main{font-size:62px;}
  .brand-sub{font-size:30px;letter-spacing:1px;}
  .panel-text{font-family:"Roboto Condensed",sans-serif;font-weight:900;}
  .claim-small{fill:var(--foam);font-size:24px;}
  .claim-big{fill:var(--foam);font-size:46px;}
  .claim-mid{fill:var(--foam);font-size:38px;}
  .program-title{fill:var(--navy);font-size:27px;}
  .program-desc{fill:var(--navy);font-size:11.5px;font-weight:800;}
  .price-euro{fill:var(--navy);font-size:13px;}
  .price-value{fill:var(--navy);font-size:15px;}
  .hours-label{fill:var(--hours-red);font-size:8px;}
  .hours-line{fill:var(--hours-red);font-size:14px;}
  .bonus-label{fill:var(--sun);font-size:9px;}
  .bonus-count{fill:var(--foam);font-size:22px;}
  .bonus-text{fill:var(--foam);font-size:10px;}
</style>
</head>
<body>
<div class="canvas">
<svg width="780" height="1200" viewBox="0 0 780 1200" xmlns="http://www.w3.org/2000/svg">
  <defs>
    <linearGradient id="claimGradient" x1="0" y1="0" x2="0" y2="1">
      <stop offset="0" stop-color="#1a3f9a"/>
      <stop offset="1" stop-color="#0a2470"/>
    </linearGradient>
    <radialGradient id="programGradient" cx="0.5" cy="0.5" r="0.6">
      <stop offset="0" stop-color="#eaf8fd"/>
      <stop offset="0.6" stop-color="#9fdcf6"/>
      <stop offset="1" stop-color="#3fbdee"/>
    </radialGradient>
  </defs>

  <g class="sign-head">
    <circle class="ring-red" cx="399" cy="240" r="182" fill="var(--sign-red)" stroke="var(--sign-edge)" stroke-width="3"/>
    <circle class="ring-grey" cx="399" cy="246" r="144" fill="var(--sign-grey)"/>
    <path class="direction-arrow" d="M117 462 L191 408 L191 311 L615 311 Q641 311 641 337 L641 457 Q641 483 615 483 L191 483 L191 515 Z" fill="var(--sign-red)"/>
    <rect class="name-plate" x="192" y="305" width="417" height="144" rx="10" fill="var(--sign-grey)" stroke="var(--sign-edge)" stroke-width="3"/>
    <text class="brand-name brand-main" x="400" y="393" text-anchor="middle" textLength="363" lengthAdjust="spacingAndGlyphs">GLANZSTRASSE</text>
    <text class="brand-name brand-sub" x="410" y="432" text-anchor="middle" textLength="210" lengthAdjust="spacingAndGlyphs">AM LINDENHOF</text>
  </g>

  <g class="pylon-panel">
    <rect class="panel-frame" x="231" y="483" width="344" height="573" fill="var(--frame)"/>
    <rect class="program-field" x="246" y="491" width="309" height="556" fill="url(#programGradient)"/>
    <rect class="claim-field" x="246" y="491" width="309" height="121" fill="url(#claimGradient)"/>
    <rect class="claim-band" x="246" y="612" width="309" height="7" fill="var(--foam)"/>
    <rect class="hours-band" x="246" y="958" width="309" height="6" fill="var(--foam)"/>
    <rect class="hours-field" x="246" y="964" width="309" height="83" fill="var(--sun)"/>

    <text class="panel-text claim-small" x="400" y="522" text-anchor="middle" textLength="264" lengthAdjust="spacingAndGlyphs">LACKSCHONEND DANK</text>
    <text class="panel-text claim-big" x="403" y="564" text-anchor="middle" textLength="262" lengthAdjust="spacingAndGlyphs">SILKREN-TUFT</text>
    <text class="panel-text claim-mid" x="400" y="596" text-anchor="middle" textLength="264" lengthAdjust="spacingAndGlyphs">SCHAUMWALZEN</text>

    <g class="program">
      <text class="panel-text program-title" x="271" y="655" textLength="181" lengthAdjust="spacingAndGlyphs">BASIS WÄSCHE</text>
      <text class="panel-text program-desc" x="272" y="670" textLength="212" lengthAdjust="spacingAndGlyphs">HD-VORWÄSCHE, FELGENREINIGUNG,</text>
      <text class="panel-text program-desc" x="272" y="684" textLength="263" lengthAdjust="spacingAndGlyphs">HEIẞEN INTENSIVWÄSCHE, GLANZTROCKNUNG</text>
      <circle cx="505" cy="646" r="22" fill="var(--sun)" stroke="var(--navy)" stroke-width="2"/>
      <text class="panel-text price-euro" x="505" y="642" text-anchor="middle">€</text>
      <text class="panel-text price-value" x="505" y="657" text-anchor="middle">7.50</text>
    </g>
    <g class="program">
      <text class="panel-text program-title" x="271" y="719" textLength="204" lengthAdjust="spacingAndGlyphs">KOMFORTPFLEGE</text>
      <text class="panel-text program-desc" x="272" y="734" textLength="186" lengthAdjust="spacingAndGlyphs">HD-VORWÄSCHE, AKTIVSCHAUM,</text>
      <text class="panel-text program-desc" x="272" y="748" textLength="220" lengthAdjust="spacingAndGlyphs">FELGENREINIGUNG, INTENSIVWÄSCHE,</text>
      <text class="panel-text program-desc" x="272" y="762" textLength="110" lengthAdjust="spacingAndGlyphs">GLANZTROCKNUNG</text>
      <circle cx="505" cy="712" r="22" fill="var(--sun)" stroke="var(--navy)" stroke-width="2"/>
      <text class="panel-text price-euro" x="505" y="708" text-anchor="middle">€</text>
      <text class="panel-text price-value" x="505" y="723" text-anchor="middle">10.50</text>
    </g>
    <g class="program">
      <text class="panel-text program-title" x="271" y="796" textLength="185" lengthAdjust="spacingAndGlyphs">SPEZIALPFLEGE</text>
      <text class="panel-text program-desc" x="272" y="811" textLength="186" lengthAdjust="spacingAndGlyphs">HD-VORWÄSCHE, AKTIVSCHAUM,</text>
      <text class="panel-text program-desc" x="272" y="825" textLength="220" lengthAdjust="spacingAndGlyphs">FELGENREINIGUNG, INTENSIVWÄSCHE,</text>
      <text class="panel-text program-desc" x="272" y="839" textLength="113" lengthAdjust="spacingAndGlyphs">GLANZTROCKNUNG,</text>
      <text class="panel-text program-desc" x="272" y="853" textLength="255" lengthAdjust="spacingAndGlyphs">HOCHGLANZVERSIEGLUNG MIT LOTUSWACHS</text>
      <circle cx="505" cy="786" r="22" fill="var(--sun)" stroke="var(--navy)" stroke-width="2"/>
      <text class="panel-text price-euro" x="505" y="782" text-anchor="middle">€</text>
      <text class="panel-text price-value" x="505" y="797" text-anchor="middle">13.00</text>
    </g>
    <g class="program">
      <text class="panel-text program-title" x="271" y="890" textLength="205" lengthAdjust="spacingAndGlyphs">PREMIUMPFLEGE</text>
      <text class="panel-text program-desc" x="272" y="905" textLength="186" lengthAdjust="spacingAndGlyphs">HD-VORWÄSCHE, AKTIVSCHAUM,</text>
      <text class="panel-text program-desc" x="272" y="919" textLength="245" lengthAdjust="spacingAndGlyphs">FELGENREINIGUNG, UNTERBODENWÄSCHE,</text>
      <text class="panel-text program-desc" x="272" y="933" textLength="221" lengthAdjust="spacingAndGlyphs">INTENSIVWÄSCHE, GLANZTROCKNUNG,</text>
      <text class="panel-text program-desc" x="272" y="947" textLength="255" lengthAdjust="spacingAndGlyphs">HOCHGLANZVERSIEGLUNG MIT LOTUSWACHS</text>
      <circle cx="505" cy="881" r="22" fill="var(--sun)" stroke="var(--navy)" stroke-width="2"/>
      <text class="panel-text price-euro" x="505" y="877" text-anchor="middle">€</text>
      <text class="panel-text price-value" x="505" y="892" text-anchor="middle">15.50</text>
    </g>

    <text class="panel-text hours-label" x="273" y="999">ÖFFNUNGSZEITEN</text>
    <text class="panel-text hours-line" x="272" y="1016" textLength="139" lengthAdjust="spacingAndGlyphs">MO-FR. : 08:00-19:00</text>
    <text class="panel-text hours-line" x="272" y="1032" textLength="112" lengthAdjust="spacingAndGlyphs">SA. : 07:00-19:00</text>

    <g class="bonus-card">
      <circle cx="476" cy="991" r="38" fill="var(--navy-deep)" stroke="var(--foam)" stroke-width="2"/>
      <rect x="416" y="1005" width="120" height="30" rx="4" fill="var(--navy-deep)" stroke="var(--foam)" stroke-width="2"/>
      <text class="panel-text bonus-label" x="476" y="972" text-anchor="middle" letter-spacing="1">BONUSKARTE</text>
      <text class="panel-text bonus-count" x="476" y="999" text-anchor="middle">10</text>
      <text class="panel-text bonus-text" x="476" y="1017" text-anchor="middle">AUTOWASCHEN,</text>
      <text class="panel-text bonus-text" x="476" y="1030" text-anchor="middle">1 GRATISWASCHE</text>
    </g>
  </g>
</svg>
</div>
</body>
</html>
```